Business Card Design Project

This is to go hand in hand with our stationery project.
Target Market(s)
Business Professionals in the Finance, HR and C-Level management arena. They are global companies that run enterprise technology solutions/products.
Mostly Male, mid 30's to 60's.
Industry/Entity Type
Business
Font styles to use
Other font styles liked:
- Calibri
Colors
9bcb3c
000000
1b1b1b
c4c4c4
ffffff
Requirements
Must have
- Logo
Name, title, contact details, address on the front of the card.
ABN and web address need to be on the card, along with our tag line
See | Share | Do
We also require rounded corners and for the card to be landscape please.
Our green is
C98 M0 Y93 K0
Modern, contemporary and must have white space for people to write on.
Nice to have
- Consistent elements with the stationery design.
Should not have
- No 90's waves - We want the feeling of movement but no wavey lines.

```html
<!DOCTYPE html>
<html lang="en">
<head>
<meta charset="utf-8">
<title>Novaro Partners – Business Card</title>
<link rel="stylesheet" href="https://fonts.googleapis.com/css2?family=Carlito:wght@400;700&display=swap">
<style>
  :root {
    --green: #9bcb3c;
    --black: #000000;
    --ink: #1b1b1b;
    --grey: #c4c4c4;
    --white: #ffffff;
    --card-light: #f1f2f1;
    --text-dark: #3a3a3a;
    --back-olive: #8f9a78;
    --back-text: #4f5447;
  }
  * { box-sizing: border-box; margin: 0; padding: 0; }
  html, body {
    width: 1200px; height: 800px; overflow: hidden;
    background: #2a2a2a;
    font-family: "Carlito", "Calibri", sans-serif;
  }
  .canvas {
    position: relative; width: 1200px; height: 800px;
    display: flex; align-items: center; justify-content: center; gap: 50px;
  }
  .card {
    position: relative; width: 525px; height: 300px;
    border-radius: 18px; overflow: hidden;
  }
  .card--front { background: linear-gradient(135deg, #f7f7f7 0%, var(--card-light) 60%, #e6e8e4 100%); }
  .card--back { background: linear-gradient(135deg, #8a9474 0%, var(--back-olive) 50%, #a3ae88 100%); }

  .brand { position: absolute; left: 32px; top: 38px; }
  .brand__name {
    font-size: 34px; font-weight: 700; color: var(--text-dark); line-height: 1;
  }
  .tagline { font-size: 22px; color: var(--text-dark); margin-top: 14px; letter-spacing: 0.3px; }

  .pattern-area {
    position: absolute; right: 0; bottom: 0; width: 300px; height: 190px;
    background: radial-gradient(ellipse at 60% 60%, rgba(155,203,60,0.22) 0%, rgba(155,203,60,0.08) 55%, rgba(155,203,60,0) 80%);
  }

  .person { position: absolute; right: 30px; top: 92px; text-align: right; color: var(--ink); }
  .person__name { font-size: 36px; font-weight: 400; line-height: 1; }
  .person__title { font-size: 21px; margin-top: 4px; }

  .contact {
    position: absolute; right: 30px; bottom: 26px; text-align: right;
    font-size: 15px; line-height: 1.3; color: var(--text-dark); list-style: none;
  }

  .card--back .brand__name,
  .card--back .tagline { color: var(--back-text); }
  .card--back .pattern-area {
    width: 100%; height: 100%;
    background: radial-gradient(ellipse at 70% 65%, rgba(155,203,60,0.55) 0%, rgba(155,203,60,0.2) 50%, rgba(155,203,60,0) 85%);
  }
</style>
</head>
<body>
<main class="canvas">
  <section class="card card--front" aria-label="Business card front">
    <div class="pattern-area" role="img" aria-label="Faint green pattern of connected rings"></div>
    <div class="brand">
      <p class="brand__name">Novaro Partners</p>
      <p class="tagline">Plan, Build, Grow</p>
    </div>
    <div class="person">
      <h1 class="person__name">Jordan Hale</h1>
      <p class="person__title">marketing manager</p>
    </div>
    <ul class="contact">
      <li>j.hale@novaro.example</li>
      <li>mobile: 086 010 000 000</li>
      <li>fax: 086 010 000 000</li>
      <li>www.novaro.example</li>
    </ul>
  </section>

  <section class="card card--back" aria-label="Business card back">
    <div class="pattern-area" role="img" aria-label="Green pattern of connected rings across the card"></div>
    <div class="brand">
      <p class="brand__name">Novaro Partners</p>
      <p class="tagline">Plan, Build, Grow</p>
    </div>
  </section>
</main>
</body>
</html>
```